Dental Design, very professional and noticable

Tindale Ridge Dental Surgery is based in Pelican Waters. We are a fast growing dental surgery and are looking for some professional business cards to send to patients.
We would like to see a design that is Vertical and uses the colours Soft Blue, Silver, White and Black. Maybe a full blue side with moto and details on back? Any other ideas or colours that you may think will make the card look unique is fine.
We need all details on the card that are listed above

Target Market(s)

Families, Retired, Other Professionals and Businesses

Industry/Entity Type

Dental

Contact Information for Business Card

Tindale Ridge Dental Surgery
Family, Cosmetic, Preventative
Dr. Owen Castrey
Dental Surgeon
BDS (Adel) FAE FADI FICD FPFA
phone: (07)50001846
fax: (07)50002917
email: tindaleridgedental@quillpost.com
http://tindaleridgedental.com/

Logo Text

Logo styles of interest
Abstract Logo
Requirements
Must have
• Vertical, Vibrant but Professional, Rounded Edges, Logo on front and back of card (different colours on each side)
Nice to have
• One side completely blue (not sure what shade) with logo and moto on bottom
Other side white, with blue or different coloured logo with details in black and silver?
Logo should show half circle with 1 end as arrow symbolizing pelican waters canal also a magnifine glass also half circled with 1 end as arrow. Any other ideas are welcome.
Should not have
• A tooth. A smile. Toothbrush or Toothpaste. Cornered edges.

```html
<!DOCTYPE html>
<html lang="en">
<head>
<meta charset="utf-8">
<title>Tindale Ridge Dental Surgery – Business Card</title>
<link href="https://fonts.googleapis.com/css2?family=Marcellus&family=Open+Sans:ital,wght@0,400;0,600;0,700;1,700&display=swap" rel="stylesheet">
<style>
  :root {
    --navy: #003a5c;
    --gold: #a68a3a;
    --paper: #f4f4f4;
    --white: #ffffff;
    --stage: #e9e6e1;
  }
  * { box-sizing: border-box; margin: 0; padding: 0; }
  html, body { width: 1200px; height: 1000px; overflow: hidden; }
  body {
    background: var(--stage);
    font-family: "Open Sans", Arial, sans-serif;
    position: relative;
  }
  .card {
    position: absolute;
    top: 110px;
    width: 440px;
    height: 780px;
    background: var(--navy);
    border-radius: 44px;
    overflow: hidden;
    box-shadow: 0 10px 28px rgba(0,0,0,0.25);
  }
  .card--front { left: 90px; }
  .card--back { left: 670px; }

  .panel {
    position: absolute;
    top: 0;
    left: 38px;
    right: 0;
    background: var(--paper);
    border-radius: 0 0 44px 44px;
  }
  .card--front .panel { height: 290px; }
  .card--back .panel { height: 610px; right: 0; }

  .brand {
    position: absolute;
    left: 0; right: 0;
    text-align: center;
  }
  .brand-mark {
    display: block;
    margin: 0 auto 14px;
    width: 54px; height: 54px;
    border-radius: 50%;
  }
  .brand-name {
    font-family: "Marcellus", Georgia, serif;
    font-size: 25px;
    line-height: 1.2;
  }
  .brand-tagline {
    font-size: 16px;
    font-weight: 600;
    margin-top: 10px;
    letter-spacing: 0.3px;
  }
  .card--front .brand { top: 90px; color: var(--gold); }
  .card--front .brand-mark { background: var(--gold); }
  .card--front .brand-name { font-size: 26px; }

  .card--back .brand { top: 640px; left: 38px; color: var(--white); }
  .card--back .brand-mark { background: var(--white); width: 40px; height: 40px; margin-bottom: 10px; }
  .card--back .brand-name { font-size: 19px; }
  .card--back .brand-tagline { font-size: 12px; margin-top: 6px; }

  .person {
    position: absolute;
    top: 196px; left: 74px;
    display: flex; align-items: center; gap: 18px;
  }
  .person-figure {
    width: 62px; height: 74px;
    border-radius: 30px 30px 8px 8px;
    background: var(--gold);
    flex: none;
  }
  .person-name {
    color: var(--navy);
    font-size: 27px;
    font-weight: 700;
    line-height: 1.1;
  }
  .person-role {
    color: var(--navy);
    font-size: 15px;
    font-weight: 700;
    font-style: italic;
    margin-top: 4px;
  }
  .person-creds {
    color: var(--navy);
    font-size: 15px;
    letter-spacing: 3px;
    margin-top: 2px;
  }

  .contacts {
    position: absolute;
    top: 340px; left: 74px; right: 24px;
    list-style: none;
  }
  .contact {
    display: flex; align-items: center;
    height: 62px;
    margin-bottom: 6px;
    color: var(--navy);
  }
  .contact svg { width: 40px; height: 40px; flex: none; margin-right: 26px; }
  .contact-phone { font-size: 18px; letter-spacing: 1.5px; }
  .contact-web { font-size: 15px; }
  .contact-mail { font-size: 14.5px; }
</style>
</head>
<body>

<section class="card card--front" aria-label="Card front">
  <div class="panel">
    <div class="brand">
      <span class="brand-mark"></span>
      <p class="brand-name">Tindale Ridge Dental Surgery</p>
      <p class="brand-tagline">Family, Cosmetic, Preventive</p>
    </div>
  </div>
</section>

<section class="card card--back" aria-label="Card back">
  <div class="panel">
    <div class="person">
      <div class="person-figure" role="img" aria-label="Icon of a dentist wearing a head lamp"></div>
      <div>
        <p class="person-name">Dr. Owen Castrey</p>
        <p class="person-role">Dental Surgeon BDS (Adel)</p>
        <p class="person-creds">FAE FADI FICD FPFA</p>
      </div>
    </div>

    <ul class="contacts">
      <li class="contact">
        <svg viewBox="0 0 40 40" aria-hidden="true"><path fill="var(--gold)" d="M12 6c2-1 4 0 5 2l2 5c1 2 0 3-1 4l-2 1c1 4 4 7 7 8l1-2c1-1 3-2 4-1l5 2c2 1 3 3 2 5l-1 2c-1 2-4 3-7 2C16 31 9 24 7 14c-1-3 0-6 2-7z"/></svg>
        <span class="contact-phone">(07)50001846</span>
      </li>
      <li class="contact">
        <svg viewBox="0 0 40 40" aria-hidden="true"><rect x="11" y="6" width="18" height="10" fill="var(--gold)"/><rect x="5" y="14" width="30" height="20" rx="3" fill="var(--gold)"/><rect x="11" y="24" width="18" height="3" fill="var(--paper)"/></svg>
        <span class="contact-phone">(07)50002917</span>
      </li>
      <li class="contact">
        <svg viewBox="0 0 40 40" aria-hidden="true"><rect x="2" y="4" width="36" height="32" rx="6" fill="var(--gold)"/><g fill="none" stroke="var(--paper)" stroke-width="1.6"><circle cx="20" cy="20" r="11"/><ellipse cx="20" cy="20" rx="5" ry="11"/><path d="M9 20h22M11 14h18M11 26h18"/></g></svg>
        <span class="contact-web">tindaleridgedental.com</span>
      </li>
      <li class="contact">
        <svg viewBox="0 0 40 40" aria-hidden="true"><rect x="3" y="8" width="34" height="24" rx="4" fill="var(--gold)"/><path d="M5 11l15 11 15-11" fill="none" stroke="var(--paper)" stroke-width="2"/></svg>
        <span class="contact-mail">tindaleridgedental@quillpost.com</span>
      </li>
    </ul>
  </div>

  <div class="brand">
    <span class="brand-mark"></span>
    <p class="brand-name">Tindale Ridge Dental Surgery</p>
    <p class="brand-tagline">Family, Cosmetic, Preventive</p>
  </div>
</section>

</body>
</html>
```